Moulding supply company needs a Door Hanger Design

Door Hanger Design Request from Ledge Craft
www. ledgecrafts.ca
We are moulding factory outlet in Toronto. Provide high quality moulding materials with competitive price like crown mouldings, casings, wainscoting, flatstocks, baseboards. We also provide professional installation for our clients. This door hanger will help the home owner easily find a local factory supplier with providing the materials as well as installation.

Detail request for design:
Size: 4”x11”, vertical
Shape: Rectangle

Content:
Front
1. Logo, see attachment(Use the left one, horizontal one)
2. Moulding factory outlet direct sale
3. Supply high quality Crown mouldings, baseboards, casings and wainscotings with competitive price
4. Installation & delivery
#2 content is the most important content, should be bold and readable
#3 can be smaller font compare to #2

Address: 47 West Falcon Ridge Rd, Richmond Hill, ON L4C 2H8
Telephone: 416 555 0143
416 555 0178
Email: info@ledgecrafts.ca

Back
Slogan: Convert plain room into designer’s interiors

Telephone: 416 555 0143
416 555 0178
Email: info@ledgecrafts.ca

Images:
Front
1. Display our productions for crown mouldings, baseboards, casings and wainscotings, refer to our website www.ledgecrafts.ca. (The winner finally we will provide the high resolution images, low resolution please copy from our website so far)
Back
2. Display 4-6 nice images for 1. wainscoting walls 2. feature walls, 3. waffle ceiling like attached below. BUT PLEASE DON'T USE THE IMAGES PROVIDED, THIS IS ONLY A SAMPLE. Please use high resolution images for printing. ALSO PLEASE DON'T LIMIT YOUR CREATIVITY TO USE 4 SQUARES LIKE BELOW IMAGES. Please provide more ideas

Note:
1. Please do the bleeding for final printing production
2. Images have to be high resolution for ready to print
3. Style need to be fresh, clean, easy to read, modern and magazine style
4. Information has to be readable, easy to find, front and back both need to display company address, telephone, email, you can use icon or abbreviation to do these information.

Thanks,
Ledge Crafts

```html
<!DOCTYPE html>
<html lang="en">
<head>
<meta charset="utf-8">
<title>Ledge Crafts – Door Hanger</title>
<link rel="stylesheet" href="https://fonts.googleapis.com/css2?family=Roboto+Condensed:ital,wght@0,300;0,400;0,700;1,300&display=swap">
<style>
  :root {
    --page: #2b2622;
    --blue: #2a4fa2;
    --orange: #f05a28;
    --white: #ffffff;
    --slate: #5b6771;
    --ink: #1d1d1d;
    --font: "Roboto Condensed", "Arial Narrow", sans-serif;
  }
  * { margin: 0; padding: 0; box-sizing: border-box; }
  html, body { width: 1200px; height: 1200px; overflow: hidden; }
  body { background: var(--page); font-family: var(--font); position: relative; }

  .hanger { position: absolute; top: 55px; width: 411px; height: 1090px; overflow: hidden; }
  .hanger--front { left: 139px; }
  .hanger--back { left: 638px; }
  .hanger__art { position: absolute; inset: 0; width: 411px; height: 1090px; display: block; }
  .layer { position: absolute; left: 0; width: 100%; text-align: center; color: var(--white); text-transform: uppercase; }

  /* front */
  .brand { position: absolute; left: 38px; top: 402px; display: flex; align-items: flex-start; gap: 14px; }
  .brand__square { width: 54px; height: 54px; background: var(--orange); flex: none; }
  .brand__name { font-weight: 400; font-size: 40px; line-height: 40px; letter-spacing: 2px; color: var(--slate); text-transform: uppercase; }
  .brand__tag { font-weight: 400; font-size: 12px; letter-spacing: 3.2px; color: var(--slate); margin-top: 8px; text-transform: uppercase; }

  .headline-pill {
    position: absolute; left: 26px; top: 479px; width: 363px; height: 62px;
    background: var(--blue); border: 2px solid var(--white); border-radius: 31px;
    display: flex; flex-direction: column; justify-content: center; align-items: center;
    color: var(--white); font-weight: 700; font-size: 27px; line-height: 26px; text-transform: uppercase;
  }

  .offer-box {
    position: absolute; left: 35px; top: 849px; width: 340px; height: 99px;
    border: 1.5px solid var(--white); border-radius: 12px;
    display: flex; flex-direction: column; justify-content: center; align-items: center;
    color: var(--white); text-transform: uppercase; text-align: center;
  }
  .offer-box__lead { font-weight: 700; font-size: 19px; line-height: 20px; }
  .offer-box__list { font-weight: 700; font-size: 23px; line-height: 22px; }
  .offer-box__note { font-weight: 300; font-style: italic; font-size: 18px; line-height: 21px; }

  .contact__address { font-weight: 300; font-size: 16.5px; line-height: 20px; }
  .contact__phones { font-weight: 700; font-size: 32px; line-height: 36px; }
  .contact__email { font-weight: 700; font-size: 24px; line-height: 28px; text-transform: none; }

  /* back */
  .badge { position: absolute; left: 0; width: 100%; top: 498px; display: flex; flex-direction: column; align-items: center; color: var(--white); }
  .badge__square { width: 58px; height: 58px; border: 6px solid var(--white); }
  .badge__name { margin-top: 10px; font-weight: 400; font-size: 28px; line-height: 30px; letter-spacing: 2px; text-transform: uppercase; }
  .badge__tag { font-size: 9px; letter-spacing: 2px; text-transform: uppercase; }

  .slogan__lead { font-weight: 300; font-size: 25px; line-height: 26px; color: var(--ink); }
  .slogan__main { font-weight: 700; font-size: 34px; line-height: 36px; }
</style>
</head>
<body>

<!-- Front -->
<section class="hanger hanger--front">
  <svg class="hanger__art" viewBox="0 0 662 1755" preserveAspectRatio="none" xmlns="http://www.w3.org/2000/svg">
    <defs>
      <linearGradient id="front-wall" x1="0" y1="0" x2="0" y2="1">
        <stop offset="0" stop-color="#4a403c"/>
        <stop offset="0.45" stop-color="#6f6865"/>
        <stop offset="0.8" stop-color="#cfcfcf"/>
        <stop offset="1" stop-color="#ececec"/>
      </linearGradient>
      <linearGradient id="front-crown" x1="0" y1="0" x2="1" y2="1">
        <stop offset="0" stop-color="#c9c9c9"/>
        <stop offset="0.5" stop-color="#8f8a86"/>
        <stop offset="1" stop-color="#a9a6a3"/>
      </linearGradient>
    </defs>
    <rect width="662" height="920" fill="url(#front-wall)" role="img" aria-label="Photo of a dark panelled wainscoting wall with a white textured vase"/>
    <path d="M0,920 Q331,760 662,920 L662,1210 Q331,1400 0,1210 Z" fill="url(#front-crown)" role="img" aria-label="Photo of white crown moulding at a ceiling corner"/>
    <path d="M0,880 Q331,730 662,915" fill="none" stroke="#ffffff" stroke-width="14"/>
    <path d="M0,1205 Q331,1420 662,1195 L662,1568 L0,1568 Z" fill="#f05a28"/>
    <path d="M0,1215 Q331,1400 662,1222 L662,1568 L0,1568 Z" fill="#2a4fa2"/>
    <rect y="1568" width="662" height="6" fill="#ffffff"/>
    <rect y="1574" width="662" height="181" fill="#f05a28"/>
    <circle cx="331" cy="292" r="130" fill="#2b2622"/>
  </svg>

  <div class="brand">
    <div class="brand__square"></div>
    <div>
      <div class="brand__name">Ledge Crafts</div>
      <div class="brand__tag">For all types of projects</div>
    </div>
  </div>

  <div class="headline-pill">
    <span>Moulding Factory Outlet</span>
    <span>Direct Sale</span>
  </div>

  <div class="offer-box">
    <span class="offer-box__lead">Supply high quality</span>
    <span class="offer-box__list">Crown mouldings, baseboards,</span>
    <span class="offer-box__list">casings and wainscotings</span>
    <span class="offer-box__note">with competitive price</span>
  </div>

  <div class="layer contact" style="top: 988px;">
    <p class="contact__address">47 West Falcon Ridge Rd, Richmond Hill, ON L4C 2H8</p>
    <p class="contact__phones">416 555 0143 / 416 555 0178</p>
    <p class="contact__email">info@ledgecrafts.ca</p>
  </div>
</section>

<!-- Back -->
<section class="hanger hanger--back">
  <svg class="hanger__art" viewBox="0 0 662 1755" preserveAspectRatio="none" xmlns="http://www.w3.org/2000/svg">
    <defs>
      <linearGradient id="back-hall" x1="0" y1="0" x2="0" y2="1">
        <stop offset="0" stop-color="#cfcfcd"/>
        <stop offset="1" stop-color="#9c9c9a"/>
      </linearGradient>
      <linearGradient id="back-feature" x1="0" y1="0" x2="1" y2="1">
        <stop offset="0" stop-color="#3a3a3a"/>
        <stop offset="0.7" stop-color="#5b5b5b"/>
        <stop offset="1" stop-color="#d6d6d4"/>
      </linearGradient>
      <linearGradient id="back-ceiling" x1="0" y1="0" x2="0" y2="1">
        <stop offset="0" stop-color="#e6e3df"/>
        <stop offset="0.6" stop-color="#d9c9b8"/>
        <stop offset="1" stop-color="#c8ab92"/>
      </linearGradient>
    </defs>
    <rect width="662" height="900" fill="url(#back-hall)" role="img" aria-label="Photo of a grey hallway with wainscoting panels and wall sconces"/>
    <path d="M0,395 C200,335 520,370 662,600 L662,900 L0,900 Z" fill="url(#back-feature)" role="img" aria-label="Photo of a living room with a dark damask feature wall and a grey sofa"/>
    <path d="M0,392 C200,332 520,367 662,597" fill="none" stroke="#ffffff" stroke-width="16"/>
    <rect y="1150" width="662" height="405" fill="url(#back-ceiling)" role="img" aria-label="Photo of a white coffered waffle ceiling with a crystal chandelier"/>
    <path d="M0,850 C150,705 460,675 662,835 C470,735 200,730 0,905 Z" fill="#2a4fa2"/>
    <ellipse cx="331" cy="1010" rx="445" ry="302" fill="#f05a28"/>
    <rect y="1553" width="662" height="202" fill="#2a4fa2"/>
    <circle cx="331" cy="292" r="130" fill="#2b2622"/>
  </svg>

  <div class="badge">
    <div class="badge__square"></div>
    <div class="badge__name">Ledge Crafts</div>
    <div class="badge__tag">For all types of projects</div>
  </div>

  <div class="layer slogan" style="top: 670px;">
    <p class="slogan__lead">Convert plain room into</p>
    <p class="slogan__main">Designer’s Interiors</p>
  </div>

  <div class="layer contact" style="top: 978px;">
    <p class="contact__address">47 West Falcon Ridge Rd, Richmond Hill, ON L4C 2H8</p>
    <p class="contact__phones">416 555 0143 / 416 555 0178</p>
    <p class="contact__email">info@ledgecrafts.ca</p>
  </div>
</section>

</body>
</html>
```